Local Healthy meal delivery service needs a new flyer

Looking for a fresh and modern flyer design for a company called "Quillmarsh Fresh Co". We provide healthy and delicious meals to families, business offices and health care workers. We would like to see designs that communicate freshness, convenience, non contact delivery and customizable meal plan options. We would like to see designs that mirror our website colors, look and feel: quillmarshfreshco.com

Target Market(s)

Families, Business Offices, Health care workers

Requirements
Must have
• Color scheme and layout matching our brand and website
Our Logo
Modern clean/professional look
contact info: website, phone number, social media
Appropriate photos
Nice to have
• "How it Works" Summary

```html
<!DOCTYPE html>
<html lang="en">
<head>
<meta charset="utf-8">
<title>Quillmarsh Fresh Co – Meal Delivery Flyer</title>
<link rel="stylesheet" href="https://fonts.googleapis.com/css2?family=Lato:wght@400;700;900&family=Teko:wght@400;500&display=swap">
<style>
  :root {
    --green: #6b9a2a;
    --green-light: #8cc63f;
    --ink: #1d1d1b;
    --white: #ffffff;
  }
  * { margin: 0; padding: 0; box-sizing: border-box; }
  html, body { width: 902px; height: 1200px; overflow: hidden; background: #e6e6e6; }
  .flyer {
    position: relative; width: 902px; height: 1200px; overflow: hidden;
    background: linear-gradient(180deg, #f6f6f4, #e9e9e6);
    font-family: "Lato", sans-serif; color: var(--ink);
  }
  .abs { position: absolute; }

  /* top dark panel */
  .hero-panel {
    left: 0; top: 0; width: 570px; height: 559px;
    background: linear-gradient(135deg, #4d4843 0%, #37332f 60%, #2f2b28 100%);
    clip-path: polygon(0 0, 565px 0, 459px 559px, 0 559px);
  }
  .hero-produce {
    left: 340px; top: 0; width: 230px; height: 559px;
    background: radial-gradient(circle at 70% 45%, rgba(140,40,30,.55) 0 60px, transparent 90px),
                radial-gradient(circle at 60% 25%, rgba(60,90,40,.55) 0 55px, transparent 85px),
                radial-gradient(circle at 60% 85%, rgba(150,50,35,.5) 0 55px, transparent 80px);
    clip-path: polygon(0 0, 225px 0, 119px 559px, 0 559px);
  }
  .badge-band {
    left: 0; top: 57px; width: 560px; height: 131px; background: var(--green);
    clip-path: polygon(0 0, 554px 0, 529px 131px, 0 131px);
  }
  .badges { list-style: none; }
  .badge { position: absolute; display: flex; align-items: center; gap: 14px; color: var(--white); font-weight: 700; font-size: 20px; white-space: nowrap; }
  .badge svg { width: 42px; height: 42px; flex: none; }
  .badge-local { left: 47px; top: 77px; }
  .badge-fresh { left: 183px; top: 77px; }
  .badge-natural { left: 319px; top: 77px; }
  .badge-gmo { left: 47px; top: 126px; }
  .badge-antibiotics { left: 233px; top: 126px; }

  .pitch { left: 47px; top: 234px; font-family: "Teko", sans-serif; color: var(--white); text-transform: uppercase; line-height: 1; font-weight: 400; }
  .pitch-lead { font-size: 82px; letter-spacing: 1px; }
  .pitch-line { font-size: 45px; margin-top: 16px; }
  .pitch-lead + .pitch-line { margin-top: 8px; }
  .pitch-line.accent { color: var(--green-light); }

  /* brand mark */
  .brand { left: 596px; top: 44px; width: 230px; height: 180px; display: flex; flex-direction: column; align-items: center; justify-content: center; gap: 10px; }
  .brand-dot { width: 30px; height: 30px; border-radius: 50%; background: var(--green); }
  .brand-name { font-weight: 900; font-size: 27px; color: var(--ink); text-align: center; line-height: 1.15; text-transform: uppercase; }

  .how-title { left: 545px; top: 264px; width: 320px; text-align: center; font-weight: 900; font-size: 34px; text-transform: uppercase; }
  .how-title span, .green { color: var(--green); }
  .step { left: 518px; display: flex; gap: 22px; width: 370px; }
  .step svg { width: 90px; height: 90px; flex: none; }
  .step h3 { font-weight: 900; font-size: 20px; margin-top: 12px; text-transform: uppercase; }
  .step p { font-size: 15px; line-height: 1.3; margin-top: 8px; }

  /* photo strip */
  .strip { left: 0; top: 559px; width: 902px; height: 227px; background: var(--white); }
  .photo { position: absolute; top: 0; height: 227px; }
  .photo-1 { left: 0; width: 240px; background: linear-gradient(135deg, #8a5a34, #c08b4a 50%, #6d8f3a); clip-path: polygon(0 0, 240px 0, 224px 227px, 0 227px); }
  .photo-2 { left: 234px; width: 236px; background: linear-gradient(135deg, #d8d3cc, #efe9e4 50%, #b9a7a0); clip-path: polygon(16px 0, 236px 0, 220px 227px, 0 227px); }
  .photo-3 { left: 464px; width: 236px; background: linear-gradient(135deg, #c9bfae, #e8e6e2 50%, #8fa4b7); clip-path: polygon(16px 0, 236px 0, 220px 227px, 0 227px); }
  .photo-4 { left: 694px; width: 208px; background: linear-gradient(135deg, #8a5c3a, #a9c08a 55%, #3f7fb8); clip-path: polygon(16px 0, 208px 0, 208px 227px, 0 227px); }

  /* lower left */
  .lower-panel {
    left: 0; top: 786px; width: 400px; height: 414px;
    background: linear-gradient(160deg, #2f3a2a, #1f241c 70%);
    clip-path: polygon(0 0, 392px 0, 333px 414px, 0 414px);
  }
  .meal-prep { left: 38px; top: 802px; width: 316px; color: var(--white); }
  .meal-prep h2 { font-weight: 900; font-size: 20px; text-transform: uppercase; }
  .meal-prep h2 span, .lifestyle h2 span { color: var(--green-light); }
  .meal-prep p { font-size: 14px; line-height: 1.3; margin-top: 10px; text-align: justify; }
  .lifestyle { left: 38px; top: 960px; width: 170px; color: var(--white); }
  .lifestyle h2 { font-weight: 900; font-size: 17px; text-transform: uppercase; white-space: nowrap; }
  .lifestyle p { font-size: 14px; line-height: 1.3; margin-top: 12px; width: 130px; }
  .dish { width: 130px; height: 78px; border: 3px solid var(--white); }
  .dish-1 { left: 233px; top: 932px; background: linear-gradient(135deg, #e8e2d8, #b4462f 55%, #5d8f33); }
  .dish-2 { left: 215px; top: 1022px; background: linear-gradient(135deg, #eee6d6, #cf9a64 50%, #6c9a3a); }
  .care-band {
    left: 0; top: 1092px; width: 340px; height: 108px; background: var(--green);
    clip-path: polygon(0 0, 340px 0, 333px 108px, 0 108px);
  }
  .care { left: 38px; top: 1110px; display: flex; align-items: center; gap: 22px; color: var(--white); font-weight: 700; font-size: 14px; line-height: 1.3; width: 290px; }
  .care svg { width: 58px; height: 58px; flex: none; }

  /* lower right */
  .order-band { left: 399px; top: 793px; width: 503px; height: 125px; background: var(--green); clip-path: polygon(6px 0, 503px 0, 503px 125px, 0 125px); }
  .order-title { left: 440px; top: 806px; font-weight: 900; font-size: 24px; color: var(--ink); text-transform: uppercase; }
  .order-title span { color: var(--white); margin-left: 8px; }
  .order-copy { left: 428px; top: 849px; width: 460px; color: var(--white); font-size: 18px; line-height: 1.3; text-align: center; }

  .contact-pill { left: 522px; top: 935px; width: 208px; height: 40px; border-radius: 10px; background: var(--green); color: var(--white); font-weight: 900; font-size: 20px; display: flex; align-items: center; justify-content: center; text-transform: uppercase; }
  .contact-pill::after { content: ""; position: absolute; left: 95px; bottom: -9px; border: 9px solid transparent; border-top-color: var(--green); border-bottom: 0; }
  .contact-line { display: flex; align-items: center; gap: 12px; font-weight: 900; color: var(--ink); white-space: nowrap; }
  .contact-line svg { width: 18px; height: 18px; flex: none; }
  .phone { left: 512px; top: 1002px; font-size: 25px; }
  .web { left: 460px; top: 1039px; font-size: 19px; }
  .mail { left: 450px; top: 1073px; font-size: 19px; }
  .social { left: 502px; top: 1122px; display: flex; gap: 34px; }
  .social-item { display: flex; align-items: center; gap: 8px; font-weight: 700; font-size: 16px; color: var(--ink); }
  .social-item i { width: 22px; height: 22px; background: var(--green); display: block; }
</style>
</head>
<body>
<main class="flyer">
  <div class="abs hero-panel" role="img" aria-label="Dark wooden table with fresh vegetables"></div>
  <div class="abs hero-produce" role="img" aria-label="Cucumbers and tomatoes on the table"></div>

  <div class="abs badge-band"></div>
  <ul class="badges">
    <li class="badge badge-local"><svg viewBox="0 0 46 46"><circle cx="23" cy="23" r="21" fill="none" stroke="#fff" stroke-width="2.5"/><path d="M23 12a7 7 0 0 1 7 7c0 6-7 14-7 14s-7-8-7-14a7 7 0 0 1 7-7z" fill="#fff"/></svg>Local</li>
    <li class="badge badge-fresh"><svg viewBox="0 0 46 46"><circle cx="23" cy="23" r="21" fill="none" stroke="#fff" stroke-width="2.5"/><circle cx="23" cy="25" r="9" fill="#fff"/><path d="M23 16c0-4 3-5 5-5" stroke="#fff" stroke-width="2.5" fill="none"/></svg>Fresh</li>
    <li class="badge badge-natural"><svg viewBox="0 0 46 46"><circle cx="23" cy="23" r="21" fill="none" stroke="#fff" stroke-width="2.5"/><path d="M13 32C13 20 22 13 34 13c0 12-7 19-19 19z" fill="#fff"/></svg>All Natural</li>
    <li class="badge badge-gmo"><svg viewBox="0 0 46 46"><circle cx="23" cy="23" r="21" fill="none" stroke="#fff" stroke-width="2.5"/><path d="M10 10l26 26" stroke="#fff" stroke-width="2.5"/><circle cx="23" cy="23" r="7" fill="none" stroke="#fff" stroke-width="2.5"/></svg>Non-GMO</li>
    <li class="badge badge-antibiotics"><svg viewBox="0 0 46 46"><circle cx="23" cy="23" r="21" fill="none" stroke="#fff" stroke-width="2.5"/><path d="M10 10l26 26" stroke="#fff" stroke-width="2.5"/><rect x="16" y="17" width="14" height="12" rx="6" fill="none" stroke="#fff" stroke-width="2.5"/></svg>No Antibiotics</li>
  </ul>

  <h1 class="abs pitch">
    <div class="pitch-lead">We Provide</div>
    <div class="pitch-line">Healthy and delicious meals</div>
    <div class="pitch-line accent">to families, business offices</div>
    <div class="pitch-line accent">and health care workers.</div>
  </h1>

  <div class="abs brand">
    <span class="brand-dot"></span>
    <span class="brand-name">Quillmarsh<br>Fresh Co</span>
  </div>

  <h2 class="abs how-title">How it <span>Works</span></h2>
  <div class="abs step" style="top:326px">
    <svg viewBox="0 0 90 90"><circle cx="45" cy="45" r="40" fill="none" stroke="#6b9a2a" stroke-width="6"/><rect x="28" y="30" width="34" height="30" rx="3" fill="none" stroke="#6b9a2a" stroke-width="4"/><path d="M28 38h34M36 25v9M54 25v9" stroke="#6b9a2a" stroke-width="4"/><path d="M35 46h4M44 46h4M53 46h4M35 53h4M44 53h4" stroke="#6b9a2a" stroke-width="3"/></svg>
    <div><h3>Every <span class="green">Tuesday</span></h3><p>we publish 2 menus for the following week, one for each delivery day (Tuesday &amp; Thursday).</p></div>
  </div>
  <div class="abs step" style="top:434px">
    <svg viewBox="0 0 90 90"><circle cx="45" cy="45" r="40" fill="none" stroke="#6b9a2a" stroke-width="6"/><rect x="27" y="30" width="36" height="24" rx="2" fill="none" stroke="#6b9a2a" stroke-width="4"/><path d="M22 60h46" stroke="#6b9a2a" stroke-width="4"/><circle cx="45" cy="42" r="6" fill="none" stroke="#6b9a2a" stroke-width="3"/></svg>
    <div><h3>Place <span class="green">Order</span></h3><p>by Midnight on Saturday with meal plan and delivery location.</p></div>
  </div>

  <section class="abs strip">
    <div class="photo photo-1" role="img" aria-label="Hands sharing colourful fresh food on a wooden table"></div>
    <div class="photo photo-2" role="img" aria-label="Woman tossing a fresh salad in a kitchen"></div>
    <div class="photo photo-3" role="img" aria-label="Health care workers sharing a meal"></div>
    <div class="photo photo-4" role="img" aria-label="Grilled chicken salad beside dumbbells and a yoga mat"></div>
  </section>

  <div class="abs lower-panel" role="img" aria-label="Dark leafy greens background"></div>
  <div class="abs meal-prep">
    <h2>Meal Prep <span>Delivered!</span></h2>
    <p>We drop off a blue soft cooler with your name on it to your specified delivery location on the day you choose. Leave your empty cooler at the drop off location and we replace it with a fresh one on your next order.</p>
  </div>
  <div class="abs lifestyle">
    <h2>Healthy <span>Lifestyle</span></h2>
    <p>Gluten Free and Vegetarian Options Available</p>
  </div>
  <div class="abs dish dish-1" role="img" aria-label="Plated fresh salad"></div>
  <div class="abs dish dish-2" role="img" aria-label="Fresh spring rolls with dipping sauce"></div>

  <div class="abs care-band"></div>
  <div class="abs care">
    <svg viewBox="0 0 62 62"><path d="M8 24l20-8 20 8v22l-20 8-20-8z" fill="none" stroke="#1d1d1b" stroke-width="4"/><path d="M8 24l20 8 20-8M28 32v22" stroke="#1d1d1b" stroke-width="4" fill="none"/><path d="M48 14v40" stroke="#1d1d1b" stroke-width="4"/></svg>
    <span>Non contact delivery and customizable meal plan options Available</span>
  </div>

  <div class="abs order-band"></div>
  <h2 class="abs order-title">Order Online <span>With Ease</span></h2>
  <p class="abs order-copy">Order on our website in a few simple steps.<br>Choose your package, delivery day(s) and location.</p>

  <div class="abs contact-pill">Contact Us</div>
  <div class="abs contact-line phone"><svg viewBox="0 0 18 18"><circle cx="9" cy="9" r="8" fill="none" stroke="#6b9a2a" stroke-width="1.8"/><path d="M6 5l2 2-1 1c.5 1.3 1.7 2.5 3 3l1-1 2 2-1.5 1.5C8 13 5 10 4.5 6.5z" fill="#6b9a2a"/></svg>555-014-2287</div>
  <div class="abs contact-line web"><svg viewBox="0 0 18 18"><circle cx="9" cy="9" r="8" fill="none" stroke="#6b9a2a" stroke-width="1.8"/><path d="M1 9h16M9 1c3 3 3 13 0 16M9 1c-3 3-3 13 0 16" stroke="#6b9a2a" stroke-width="1.4" fill="none"/></svg>www.quillmarshfreshco.com</div>
  <div class="abs contact-line mail"><svg viewBox="0 0 18 18"><rect x="1" y="4" width="16" height="11" fill="#6b9a2a"/><path d="M1 4l8 6 8-6" stroke="#fff" stroke-width="1.4" fill="none"/></svg>hello@quillmarshfreshco.com</div>
  <div class="abs social">
    <span class="social-item"><i></i>Chatterbook</span>
    <span class="social-item"><i></i>Snapgrid</span>
  </div>
</main>
</body>
</html>
```